Torvane PT Business Card

I need the card to be bright/bold colours to stand out amongst others.
It needs to have my company logo.
I was not interested in pictures etc just a layout that attracts attention.

I have attached my old design which is very plain. I also needed change the contact details. And my description changed to Personal Trainer
Phone 0427391058
Facebook Torvane PT
No email address please, no street address.
And only Torvane PT (Please remove anything to do with Torvane Supplements)

```html
<!DOCTYPE html>
<html lang="en">
<head>
<meta charset="utf-8">
<title>Torvane PT – Business Card</title>
<link href="https://fonts.googleapis.com/css2?family=Arimo:wght@400;700&family=Jost:wght@400&display=swap" rel="stylesheet">
<style>
  :root {
    --cyan: #2ff2dc;
    --aqua: #5cf0c4;
    --mint: #a4f3a8;
    --cream: #f1fbc6;
    --brand-blue: #2b8be0;
    --text-blue: #2a78c0;
    --rule-blue: #4a86c8;
    --band: rgba(255, 255, 255, 0.12);
  }
  * { margin: 0; padding: 0; box-sizing: border-box; }
  html, body { width: 1200px; height: 685px; overflow: hidden; }
  body { background: #ffffff; }

  .card {
    position: relative;
    width: 1200px;
    height: 685px;
    overflow: hidden;
    background:
      linear-gradient(135deg, var(--cyan) 0%, var(--aqua) 18%, var(--mint) 38%, var(--cream) 58%, var(--mint) 80%, var(--cyan) 100%);
  }
  .card-bands {
    position: absolute;
    inset: 0;
    background:
      repeating-linear-gradient(60deg, transparent 0 90px, var(--band) 90px 130px, transparent 130px 210px),
      repeating-linear-gradient(-30deg, transparent 0 110px, var(--band) 110px 140px, transparent 140px 230px);
  }

  .brand-name {
    position: absolute;
    right: 83px;
    top: 80px;
    width: 508px;
    text-align: right;
    font-family: "Arimo", Arial, sans-serif;
    font-weight: 700;
    font-size: 72px;
    line-height: 1;
    letter-spacing: 2px;
    color: var(--brand-blue);
    text-transform: uppercase;
  }
  .brand-rule {
    position: absolute;
    left: 609px;
    top: 182px;
    width: 432px;
    height: 2px;
    background: var(--rule-blue);
  }

  .contact-list {
    position: absolute;
    right: 83px;
    top: 314px;
    list-style: none;
    text-align: right;
    font-family: "Arimo", Arial, sans-serif;
    font-weight: 400;
    color: var(--text-blue);
  }
  .contact-item { font-size: 33px; line-height: 57px; }
  .contact-label { font-size: 25px; margin-right: 10px; }

  .trainer {
    position: absolute;
    left: 86px;
    top: 370px;
    font-family: "Jost", Arial, sans-serif;
    font-weight: 400;
    color: var(--text-blue);
  }
  .trainer-name { font-size: 47px; line-height: 1.1; }
  .trainer-role { font-size: 25px; margin-left: 127px; line-height: 1.2; }
</style>
</head>
<body>
  <div class="card">
    <div class="card-bands"></div>

    <div class="brand-name">Torvane PT</div>
    <div class="brand-rule"></div>

    <ul class="contact-list">
      <li class="contact-item"><span class="contact-label">t |</span>0427391058</li>
      <li class="contact-item"><span class="contact-label">fb |</span>Torvane PT</li>
    </ul>

    <div class="trainer">
      <div class="trainer-name">sam harlow</div>
      <div class="trainer-role">personal trainer</div>
    </div>
  </div>
</body>
</html>
```